Modern, cutting edge crypto trading website.

I need a single-page website design, approximate 4-5 pages. I have included a screenshot of the inside of the current application for some reference for what it currently looks like. This is the public side of the application for not logged in users.

I am currently thinking about 3-5 sections of the page.
Menu at top is optional, these could be the sections of the site.
1. Above the fold cool, grabbing stuff.
2. What problem does this solve
3. Additional benefits
4. Pricing
5. Open to ideas! Well it's all open to ideas if you have ideas.

I am nervous about hiring designers, I am open to a further discussion for more work for additional money but I have to LIKE your design. So this could be considered a trial. I would like to continue to design the application itself and match everything together!

I really like the tradewisp website.

Competitor websites:
https://7ridges.example/
https://www.tradewisp.example/

Target Market(s)

Adults 25-50 mostly male,

Number of Pages Required

4 page

Colors

Designer to choose colors to be used in the design.

Requirements
Must have
• Modern design, clean lines, professional.
Nice to have
• Fun SVG stuff. Not for this price, but in the future.
Should not have
• Should not be cluttered OR too spacey. Quince's website has too much open space sometimes.

```html
<!DOCTYPE html>
<html lang="en">
<head>
<meta charset="utf-8">
<title>Tickline — Crypto Trading Tools</title>
<link href="https://fonts.googleapis.com/css2?family=Nunito+Sans:wght@400;600;700&display=swap" rel="stylesheet">
<style>
:root{
  --blue:#1f7fcc;
  --blue-btn:#2a78d0;
  --sky:#4fb8f0;
  --mid:#2f84de;
  --navy:#333f8a;
  --cta-a:#3e63b0;
  --cta-b:#3a5aa8;
  --cta-c:#3b4f9c;
  --ink:#1c2340;
  --text:#2b2f3a;
  --white:#ffffff;
  --card-shadow:0 6px 24px rgba(40,60,120,.10);
}
*{margin:0;padding:0;box-sizing:border-box}
html,body{width:1200px;height:2708px;overflow:hidden}
body{position:relative;font-family:"Nunito Sans",Arial,sans-serif;color:var(--text);background:var(--white)}
.btn{position:absolute;display:flex;align-items:center;justify-content:center;border-radius:14px;font-size:11px;font-weight:700;text-decoration:none}
.btn-blue{background:var(--blue-btn);color:var(--white);box-shadow:0 4px 10px rgba(42,120,208,.35)}
.btn-white{background:var(--white);color:var(--blue-btn);box-shadow:0 4px 10px rgba(0,0,0,.15)}

/* nav */
.nav{position:absolute;left:0;top:0;width:1200px;height:56px;background:var(--white);box-shadow:0 2px 6px rgba(0,0,0,.05);z-index:5}
.brand{position:absolute;left:88px;top:16px;display:flex;align-items:center;gap:8px;font-size:16px;font-weight:600;color:var(--blue);letter-spacing:.5px}
.brand-mark{width:22px;height:22px;border-radius:4px;background:var(--blue)}
.menu{position:absolute;right:198px;top:21px;display:flex;gap:28px;font-size:10.5px;color:var(--ink);letter-spacing:.3px}

/* hero */
.hero-title{position:absolute;left:0;width:1200px;top:104px;text-align:center;font-size:32px;line-height:37px;font-weight:400;color:var(--blue)}
.hero-sub{position:absolute;left:0;width:1200px;top:192px;text-align:center;font-size:14px;line-height:18px;color:var(--ink)}
.waves{position:absolute;left:0;top:0;width:1200px;height:1090px}
.laptop{position:absolute;left:395px;top:310px;width:420px;height:290px}

/* problem */
.problem-title{position:absolute;left:88px;top:750px;width:420px;font-size:22px;line-height:27px;color:var(--white);font-weight:400}
.problem-text{position:absolute;left:88px;top:852px;width:420px;font-size:11.5px;line-height:17.5px;color:var(--white);font-weight:600}
.problem-text p{margin-bottom:9px}
.problem-art{position:absolute;left:640px;top:705px;width:420px;height:340px;border-radius:40px;background:radial-gradient(circle at 50% 45%,#3fd6a6 0,#3a7fe0 30%,#3a48a0 65%,rgba(51,63,138,0) 80%)}

/* features */
.section-title{position:absolute;left:0;width:1200px;top:1138px;text-align:center;font-size:21px;font-weight:400;color:var(--blue)}
.section-desc{position:absolute;left:0;width:1200px;top:1176px;text-align:center;font-size:13px;line-height:18px;color:var(--ink)}
.features-deco{position:absolute;left:1148px;top:1180px;width:60px;height:310px;font-size:60px;font-weight:700;color:#eef0f4;writing-mode:vertical-rl;transform:rotate(180deg);line-height:60px;letter-spacing:2px}
.card{position:absolute;width:328px;height:233px;background:var(--white);box-shadow:var(--card-shadow);padding:18px 18px}
.card svg{display:block;width:46px;height:46px}
.card h3{font-size:14px;font-weight:400;color:var(--blue);margin:10px 0 12px}
.card p{font-size:9.8px;line-height:17.5px;color:var(--ink);margin-bottom:4px}

.split-title{position:absolute;font-size:21px;line-height:26px;font-weight:400;color:var(--blue)}
.split-text{position:absolute;width:400px;font-size:12.5px;line-height:17.5px;color:var(--ink)}
.split-text p{margin-bottom:10px}
.art{position:absolute;border-radius:50%}

/* cta */
.cta{position:absolute;left:88px;top:2236px;width:1024px;height:231px;background:linear-gradient(120deg,var(--cta-a) 0%,var(--cta-b) 50%,var(--cta-c) 100%);border-radius:4px}
.cta-title{position:absolute;left:0;width:1024px;top:60px;text-align:center;font-size:24px;font-weight:400;color:var(--white)}
.cta-sub{position:absolute;left:0;width:1024px;top:101px;text-align:center;font-size:13px;color:var(--white)}

/* footer */
.footer{position:absolute;left:0;top:2514px;width:1200px;height:194px;background:var(--navy);color:var(--white)}
.footer .brand{top:36px;color:var(--white)}
.footer .brand-mark{background:var(--white)}
.foot-about{position:absolute;left:88px;top:78px;width:240px;font-size:9.5px;line-height:19px}
.foot-copy{position:absolute;left:88px;top:146px;font-size:9.5px}
.foot-col{position:absolute;top:28px;font-size:9.5px;line-height:19px}
.foot-col h4{font-size:12px;font-weight:400;margin-bottom:10px}
</style>
</head>
<body>

<header class="nav">
  <div class="brand"><span class="brand-mark"></span>TICKLINE</div>
  <nav class="menu"><span>HOME</span><span>FEATURES</span><span>PLANS</span><span>ABOUT</span><span>CONTACT</span></nav>
  <a class="btn btn-blue" style="left:1031px;top:16px;width:81px;height:24px">Sign Up</a>
</header>

<svg class="waves" viewBox="0 0 1200 1090" aria-hidden="true">
  <path fill="var(--sky)" d="M0 420 C120 400 220 470 340 440 C520 400 700 520 880 450 C1010 400 1060 262 1200 255 L1200 1090 L0 1090Z"/>
  <path fill="var(--mid)" d="M0 470 C150 440 260 560 420 560 C620 560 760 610 900 585 C1050 560 1120 430 1200 405 L1200 1090 L0 1090Z"/>
  <path fill="var(--navy)" d="M0 480 C80 520 200 625 400 635 C700 655 1000 665 1200 585 L1200 1090 L0 1090Z"/>
</svg>

<h1 class="hero-title">Write a headline here that explains<br>your unique selling point !</h1>
<p class="hero-sub">Tools for crypto traders to grow profits, minimize<br>risks, limit losses across multiple exchanges.</p>
<a class="btn btn-blue" style="left:550px;top:250px;width:100px;height:24px">Get started</a>

<svg class="laptop" viewBox="0 0 420 290">
  <rect x="0" y="0" width="420" height="283" rx="10" fill="#e4e6ea"/>
  <rect x="5" y="4" width="410" height="270" rx="7" fill="#ffffff"/>
  <rect x="13" y="15" width="394" height="259" fill="#f3f3f1" role="img" aria-label="Application dashboard screenshot showing trading strategies"/>
  <rect x="13" y="15" width="63" height="259" fill="#111"/>
  <rect x="83" y="37" width="316" height="98" fill="#fff"/>
  <rect x="83" y="143" width="316" height="48" fill="#fff"/>
  <rect x="0" y="276" width="420" height="10" rx="5" fill="#c9ccd2"/>
</svg>

<h2 class="problem-title">Here explain what are the problems that your target audience faces that you're gonna solve !</h2>
<div class="problem-text">
  <p>Grow your portfolio like the world's most sophisticated investors. We're making institutional portfolio management software available to everyone.</p>
  <p>Lorem ipsum dolor sit amet, consectetur adipiscing elit. Mauris consectetur malesuada turpis, at condimentum tellus. Suspendisse mattis diam id odio pulvinar, non cursus odio dignissim.</p>
</div>
<a class="btn btn-white" style="left:88px;top:980px;width:81px;height:24px">Sign Up</a>
<div class="problem-art" role="img" aria-label="Isometric illustration of a glowing coin stack on a platform with bar charts"></div>

<h2 class="section-title">Features</h2>
<p class="section-desc">Here explain how your product solves the problem mentioned above. Lorem ipsum dolor sit amet,<br>consectetur adipiscing elit. Mauris consectetur malesuada turpis, at condimentum tellus.</p>
<div class="features-deco" aria-hidden="true">FEATURES</div>

<article class="card" style="left:88px;top:1260px">
  <svg viewBox="0 0 46 46" fill="none" stroke="var(--blue)" stroke-width="1.5"><path d="M23 3l8 4.5v9L23 21l-8-4.5v-9z M15 7.5L23 12l8-4.5 M23 12v9"/><path d="M13 22l8 4.5v9L13 40l-8-4.5v-9z M5 26.5L13 31l8-4.5 M13 31v9"/><path d="M33 22l8 4.5v9L33 40l-8-4.5v-9z M25 26.5L33 31l8-4.5 M33 31v9"/></svg>
  <h3>Lorem ipsum dolor</h3>
  <p>Here explain how your product solves the problem mentioned above. Lorem ipsum dolor sit amet, consectetur adipiscing elit. Mauris consectetur malesuada turpis, at condimentum tellus.</p>
  <p>Here explain how your product solves the problem mentioned above. Lorem ipsum dolor sit amet, consectetur adipiscing elit. Mauris consectetur malesuada turpis, at condimentum tellus.</p>
</article>
<article class="card" style="left:436px;top:1242px">
  <svg viewBox="0 0 46 46" fill="none" stroke="var(--blue)" stroke-width="1.5"><path d="M23 3l8 4.5v9L23 21l-8-4.5v-9z M15 7.5L23 12l8-4.5 M23 12v9"/><path d="M13 22l8 4.5v9L13 40l-8-4.5v-9z M5 26.5L13 31l8-4.5 M13 31v9"/><path d="M33 22l8 4.5v9L33 40l-8-4.5v-9z M25 26.5L33 31l8-4.5 M33 31v9"/></svg>
  <h3>Lorem ipsum dolor</h3>
  <p>Here explain how your product solves the problem mentioned above. Lorem ipsum dolor sit amet, consectetur adipiscing elit. Mauris consectetur malesuada turpis, at condimentum tellus.</p>
  <p>Here explain how your product solves the problem mentioned above. Lorem ipsum dolor sit amet, consectetur adipiscing elit. Mauris consectetur malesuada turpis, at condimentum tellus.</p>
</article>
<article class="card" style="left:784px;top:1260px">
  <svg viewBox="0 0 46 46" fill="none" stroke="var(--blue)" stroke-width="1.5"><path d="M23 3l8 4.5v9L23 21l-8-4.5v-9z M15 7.5L23 12l8-4.5 M23 12v9"/><path d="M13 22l8 4.5v9L13 40l-8-4.5v-9z M5 26.5L13 31l8-4.5 M13 31v9"/><path d="M33 22l8 4.5v9L33 40l-8-4.5v-9z M25 26.5L33 31l8-4.5 M33 31v9"/></svg>
  <h3>Lorem ipsum dolor</h3>
  <p>Here explain how your product solves the problem mentioned above. Lorem ipsum dolor sit amet, consectetur adipiscing elit. Mauris consectetur malesuada turpis, at condimentum tellus.</p>
  <p>Here explain how your product solves the problem mentioned above. Lorem ipsum dolor sit amet, consectetur adipiscing elit. Mauris consectetur malesuada turpis, at condimentum tellus.</p>
</article>

<div class="art" style="left:110px;top:1550px;width:480px;height:290px;background:radial-gradient(ellipse at 55% 45%,#f4f6fb 0,#f4f6fb 30%,#3a86e0 32%,#2f6fd0 70%,#3d8ee6 100%)" role="img" aria-label="Illustration of a person floating beside a growth chart panel"></div>
<h2 class="split-title" style="left:653px;top:1570px">Lorem ipsum dolor sit amet,<br>consectetur adipiscing elit</h2>
<div class="split-text" style="left:653px;top:1637px">
  <p>Here explain how your product solves the problem mentioned above. Lorem ipsum dolor sit amet, consectetur adipiscing elit. Mauris consectetur malesuada turpis, at condimentum tellus.</p>
  <p>Here explain how your product solves the problem mentioned above. Lorem ipsum dolor sit amet, consectetur adipiscing elit. Mauris consectetur malesuada turpis, at condimentum tellus.</p>
</div>
<a class="btn btn-blue" style="left:653px;top:1778px;width:100px;height:24px">Get started</a>

<h2 class="split-title" style="left:149px;top:1920px">Lorem ipsum dolor sit amet,<br>consectetur adipiscing elit</h2>
<div class="split-text" style="left:149px;top:1987px">
  <p>Here explain how your product solves the problem mentioned above. Lorem ipsum dolor sit amet, consectetur adipiscing elit. Mauris consectetur malesuada turpis, at condimentum tellus.</p>
  <p>Here explain how your product solves the problem mentioned above. Lorem ipsum dolor sit amet, consectetur adipiscing elit. Mauris consectetur malesuada turpis, at condimentum tellus.</p>
</div>
<a class="btn btn-blue" style="left:149px;top:2128px;width:100px;height:24px">Get started</a>
<div class="art" style="left:615px;top:1895px;width:480px;height:295px;background:radial-gradient(ellipse at 52% 48%,#f4f6fb 0,#f4f6fb 30%,#3a86e0 32%,#3f9be8 70%,#56b8f0 100%)" role="img" aria-label="Illustration of a person working with a settings and analytics panel"></div>

<section class="cta" aria-label="Call to action banner over a faint financial newspaper backdrop">
  <h2 class="cta-title">Ready to get started? Join us right now!</h2>
  <p class="cta-sub">Try Tickline free for 7 days. No credit card needed.</p>
  <a class="btn btn-white" style="left:456px;top:152px;width:86px;height:23px">Get Started</a>
</section>

<footer class="footer">
  <div class="brand"><span class="brand-mark"></span>TICKLINE</div>
  <p class="foot-about">Lorem ipsum dolor sit amet, consectetur adipiscing elit, sed do eiusmod tempor incididunt ut labore et dolore magna aliqua</p>
  <p class="foot-copy">© Copyright 2019 Tickline,&nbsp; All Right Reserved</p>
  <div class="foot-col" style="left:436px"><h4>Quick View</h4>Home<br>About<br>Services<br>Projects<br>Quote</div>
  <div class="foot-col" style="left:612px"><h4>Services</h4>Commercial Cleaning<br>House Cleaning<br>Office Cleaning<br>Glass Cleaning<br>Window Clening</div>
  <div class="foot-col" style="left:783px"><h4>Services</h4>Commercial Cleaning<br>House Cleaning<br>Office Cleaning<br>Glass Cleaning<br>Window Clening</div>
  <div class="foot-col" style="left:959px"><h4>Contact Us</h4>Phone: +1 555 010 4821<br>Email: hello@tickline.example<br>Fax: +1 555 010 7736</div>
</footer>

</body>
</html>
```